Web form face-lift for an online startup

We are a web startup building a SaaS application for the freight industry. The project is mainly dedicated to the paint the main form that our customer are using along the search results that the they get. All details are in the attached documents.
Updates
The application serves the Freight Forwarders community so please think towards this industry when using background images, banners, colors, icons, etc. Computer and technology images are irrelevant.
Customer fields at the top of the page is actually part of the form.
Target Market(s)
Usually business users (Sales people, procurement, shippers, freight forwarders). Some are less tech savvy and some appreciate the new trendy web apps.
Industry/Entity Type
Building
Colors
Designer to choose colors to be used in the design.
Look and feel
Each slider illustrates characteristics of the customer's brand and the style your logo design should communicate.

```html
<!DOCTYPE html>
<html lang="en">
<head>
<meta charset="utf-8">
<title>Cargolane – Search For Quotes</title>
<link href="https://fonts.googleapis.com/css2?family=Roboto:wght@300;400;500;700&display=swap" rel="stylesheet">
<style>
:root{
  --blue:#3598db;
  --blue-dark:#2a83c4;
  --blue-btn:#2f86c7;
  --white:#ffffff;
  --ink:#3a3a3a;
  --muted:#666666;
  --line:#c9c9c9;
  --grey-btn:#9a9a9a;
  --footer:#a8a8a8;
  --footer-ink:#6b6b6b;
  --red:#d9232a;
}
*{box-sizing:border-box;margin:0;padding:0}
html,body{width:1200px;height:921px;overflow:hidden}
body{position:relative;font-family:'Roboto',sans-serif;color:var(--ink);background:var(--white)}
.abs{position:absolute}

/* header */
.site-header{left:0;top:0;width:1200px;height:86px;background:var(--blue);border-bottom:3px solid var(--blue-dark)}
.brand{left:170px;top:30px;color:var(--white);font-weight:700;font-size:22px;letter-spacing:.5px}
.nav-icon{left:419px;top:38px;width:21px;height:21px;border:2px solid var(--white);border-radius:50%}
.main-nav{left:460px;top:40px;display:flex;gap:21px;color:var(--white);font-size:12.5px}
.utility{top:7px;color:var(--white);font-size:9.5px}
.profile{left:903px;top:0;width:129px;height:86px;background:var(--blue-dark);text-align:center}
.avatar{position:absolute;left:40px;top:7px;width:50px;height:50px;border-radius:50%;background:radial-gradient(circle at 50% 40%,#c99a82,#5a4a44);border:2px solid #e0e0e0}
.profile-name{position:absolute;left:0;right:0;top:63px;color:var(--white);font-size:12px;font-weight:500}
.profile-name::after{content:"";display:inline-block;margin-left:8px;border:5px solid transparent;border-top:6px solid #8cc8f0;vertical-align:-3px}

/* hero */
.hero{left:0;top:89px;width:1200px;height:258px;background:linear-gradient(180deg,#25303f 0%,#4a4f5c 25%,#a7683f 48%,#6b4a3a 62%,#2e3038 85%,#1f2128 100%)}
.hero-title{left:173px;top:145px;color:var(--white);font-size:19px;font-weight:300}
.hero-label{left:173px;top:181px;color:#eee;font-size:13px;font-weight:300}
.hero-input{left:240px;top:178px;width:212px;height:28px;border:1px solid #e6e6e6}
.hero-check{left:171px;top:237px;width:12px;height:12px;background:#ddd;border-radius:2px}
.hero-check-label{left:193px;top:235px;color:#eee;font-size:13px;font-weight:300}
.mode-tab{background:var(--blue);display:flex;align-items:center;justify-content:center}

/* cargo panel */
.cargo{left:0;top:347px;width:1200px;height:133px;background:var(--blue)}
.field-label{top:367px;color:var(--white);font-size:13px}
.field{top:394px;height:28px;border:1px solid #cfe6f7;color:var(--white);font-size:12.5px;display:flex;align-items:center;justify-content:center}
.unit-select{top:395px;height:27px;background:#9fa3a7;color:var(--white);font-size:14px;font-weight:500;display:flex;align-items:center}
.unit-select span{flex:1;padding-left:10px}
.unit-select i{width:26px;height:100%;border-left:1px solid #b9bcbf;display:flex;align-items:center;justify-content:center}
.caret{border:5px solid transparent;border-top:6px solid var(--white);margin-top:5px}
.add-units{left:170px;top:438px;width:127px;height:24px;background:var(--grey-btn);color:var(--white);font-size:11.5px;font-weight:500;display:flex;align-items:center;padding-left:8px;gap:8px}

/* route */
.route{left:0;top:480px;width:1200px;height:54px;border-top:1px solid #dcdcdc;border-bottom:1px solid #dcdcdc}
.route-label{top:502px;font-size:12px;font-weight:500;color:#222}
.route-input{top:493px;width:332px;height:31px;border:1px solid var(--line);font-size:12px;color:#555;padding:9px 10px}

/* options */
.options-title{left:169px;top:569px;font-size:26px;font-weight:300;color:#333}
.trade{top:623px;font-size:16px;font-weight:300;color:#333}
.sep{top:627px;height:14px;border-left:1px dotted #999}
.opt-check{top:630px;width:12px;height:12px;background:#ddd;border:1px solid #bbb;border-radius:2px}
.price-level{left:678px;top:618px;width:353px;height:35px;border:1px solid var(--line);font-size:13px;color:#444;display:flex;align-items:center}
.price-level span{flex:1;padding-left:12px}
.price-level i{width:35px;height:100%;border-left:1px solid var(--line);display:flex;align-items:center;justify-content:center}
.price-level .caret{border-top-color:#999}
.more-option{left:939px;top:660px;font-size:13px;color:#555;display:flex;align-items:center;gap:6px}

/* action */
.search-btn{left:494px;top:725px;width:214px;height:39px;background:var(--blue-btn);color:var(--white);font-size:20px;font-weight:500;display:flex;align-items:center;justify-content:center}
.alt{left:494px;width:214px;text-align:center;color:#444;font-size:12.5px}

/* footer */
.site-footer{left:0;top:857px;width:1200px;height:64px;background:var(--footer)}
.footer-link{top:883px;color:var(--footer-ink);font-size:13px}
.social{top:878px;width:23px;height:23px;border-radius:50%;background:#8a8a8a}
</style>
</head>
<body>

<header class="abs site-header">
  <div class="abs brand">CARGOLANE</div>
  <div class="abs nav-icon"></div>
  <nav class="abs main-nav">
    <span>Menu Item 1</span><span>Menu Item 2</span><span>Menu Item 3</span><span>Menu Item 4</span><span>Menu Item 5</span>
  </nav>
  <div class="abs utility" style="left:790px">USD</div>
  <div class="abs utility" style="left:834px">ENGLISH</div>
  <div class="abs profile">
    <div class="avatar" role="img" aria-label="User profile photo"></div>
    <div class="profile-name">ALEX MORROW</div>
  </div>
</header>

<section class="abs hero" role="img" aria-label="Blurred photo of a container port with cranes at sunset"></section>
<div class="abs hero-title">Search For Quotes</div>
<div class="abs hero-label">Customer</div>
<div class="abs hero-input"></div>
<div class="abs hero-check"></div>
<div class="abs hero-check-label">Rate A Quote ?</div>

<div class="abs mode-tab" style="left:498px;top:268px;width:93px;height:79px">
  <svg width="72" height="60" viewBox="0 0 72 60" fill="none" stroke="#fff" stroke-width="5" stroke-linejoin="round">
    <path d="M36 6 L66 16 L36 26 L6 16 Z"/><path d="M12 22 V44 L36 54 L60 44 V22"/><path d="M36 26 V54"/><path d="M6 16 L2 28 L30 36 L36 26"/><path d="M66 16 L70 28 L42 36 L36 26"/>
  </svg>
</div>
<div class="abs mode-tab" style="left:597px;top:285px;width:94px;height:62px">
  <svg width="62" height="44" viewBox="0 0 62 44" fill="#c6e4f8">
    <rect x="22" y="10" width="26" height="14"/><rect x="12" y="6" width="8" height="18"/><circle cx="14" cy="3" r="3"/>
    <path d="M2 24 H60 L52 40 H8 Z"/>
  </svg>
</div>
<div class="abs mode-tab" style="left:697px;top:285px;width:93px;height:62px">
  <svg width="46" height="48" viewBox="0 0 46 48" fill="#c6e4f8">
    <path d="M23 2 L43 12 L23 22 L3 12 Z"/><path d="M3 16 L21 25 V46 L3 37 Z"/><path d="M43 16 L25 25 V46 L43 37 Z"/>
  </svg>
</div>

<section class="abs cargo"></section>
<div class="abs field-label" style="left:172px">Qty</div>
<div class="abs field-label" style="left:253px">Stackable</div>
<div class="abs field-label" style="left:341px">Load</div>
<div class="abs field-label" style="left:577px">Length</div>
<div class="abs field-label" style="left:651px">Width</div>
<div class="abs field-label" style="left:728px">Height</div>
<div class="abs field-label" style="left:888px">Weight</div>

<div class="abs field" style="left:170px;width:48px">5</div>
<div class="abs" style="left:253px;top:399px;width:13px;height:13px;background:#ddd;border-radius:2px"></div>
<div class="abs field" style="left:339px;width:220px;justify-content:space-between;padding:0 12px 0 8px"><span>Box / Pallet</span><span class="caret"></span></div>
<div class="abs field" style="left:575px;width:59px">100</div>
<div class="abs field" style="left:650px;width:59px">100</div>
<div class="abs field" style="left:724px;width:59px">100</div>
<div class="abs unit-select" style="left:791px;width:76px"><span>cm</span><i><b class="caret"></b></i></div>
<div class="abs field" style="left:883px;width:59px">100</div>
<div class="abs unit-select" style="left:953px;width:78px"><span>kg</span><i><b class="caret"></b></i></div>
<div class="abs add-units">
  <svg width="14" height="14" viewBox="0 0 14 14" fill="none" stroke="#fff" stroke-width="1.3"><circle cx="7" cy="7" r="6"/><path d="M7 4v6M4 7h6"/></svg>
  Add more units
</div>

<section class="abs route"></section>
<div class="abs route-label" style="left:170px">From :</div>
<div class="abs route-input" style="left:213px">Shipping address or port</div>
<svg class="abs" style="left:589px;top:497px" width="22" height="22" viewBox="0 0 22 22" fill="none" stroke="#333" stroke-width="1.2"><circle cx="11" cy="11" r="10"/><path d="M9 6l5 5-5 5"/></svg>
<div class="abs route-label" style="left:655px">To :</div>
<div class="abs route-input" style="left:698px">Shipping address or port</div>

<h2 class="abs options-title">Options</h2>
<div class="abs trade" style="left:169px">Import</div>
<div class="abs sep" style="left:227px"></div>
<div class="abs trade" style="left:237px">Export</div>
<div class="abs sep" style="left:292px"></div>
<div class="abs trade" style="left:303px">Incoterm : <span style="color:var(--blue)">FCA</span></div>

<div class="abs opt-check" style="left:487px"></div>
<svg class="abs" style="left:506px;top:624px" width="22" height="22" viewBox="0 0 22 22" fill="none"><rect x="7" y="6" width="8" height="10" fill="#2a83c4"/><circle cx="11" cy="11" r="9.5" stroke="var(--red)" stroke-width="2"/><path d="M5 17L17 5" stroke="var(--red)" stroke-width="2"/></svg>
<div class="abs opt-check" style="left:549px"></div>
<svg class="abs" style="left:569px;top:624px" width="22" height="22" viewBox="0 0 22 22" fill="none"><path d="M6 15h10l-2 3H8z M10 8h3v7h-3z" fill="#2a83c4"/><circle cx="11" cy="11" r="9.5" stroke="var(--red)" stroke-width="2"/><path d="M5 17L17 5" stroke="var(--red)" stroke-width="2"/></svg>
<div class="abs opt-check" style="left:609px"></div>
<svg class="abs" style="left:628px;top:624px" width="22" height="22" viewBox="0 0 22 22" fill="none"><path d="M11 11L7 5h8z M11 11l7 4-3 3z M11 11l-7 4 3 3z" fill="#2a83c4"/><circle cx="11" cy="11" r="9.5" stroke="var(--red)" stroke-width="2"/><path d="M5 17L17 5" stroke="var(--red)" stroke-width="2"/></svg>

<div class="abs price-level"><span>Price Level</span><i><b class="caret"></b></i></div>
<div class="abs more-option">
  <svg width="16" height="16" viewBox="0 0 16 16" fill="none" stroke="#777" stroke-width="1.2"><circle cx="8" cy="8" r="7"/><path d="M8 4.5v7M4.5 8h7"/></svg>
  more option
</div>

<div class="abs search-btn">SEARCH QUOTES</div>
<div class="abs alt" style="top:775px">or</div>
<div class="abs alt" style="top:790px">Create manually</div>

<footer class="abs site-footer"></footer>
<div class="abs footer-link" style="left:171px">About Us</div>
<div class="abs footer-link" style="left:245px">Privacy Policy</div>
<div class="abs footer-link" style="left:350px">Terms Of service</div>
<div class="abs footer-link" style="left:473px">News</div>
<div class="abs social" style="left:881px"></div>
<div class="abs social" style="left:913px"></div>
<div class="abs social" style="left:944px"></div>
<div class="abs social" style="left:975px"></div>
<div class="abs social" style="left:1007px"></div>

</body>
</html>
```